Mobile CCTV Command Centre Brochure- Service for Hire

We need to re-do our promotional brochure for our MCCC- Mobile CCTV Command Centre. We now have better pictures of the vehicle and our existing brochure is very simple and not terribly interesting. The new brochure should be bold and exciting with better graphics. I've included the old brochure (Vantage Guard Control Base) to give designers an idea of what we already use for our hire clients. We need the additional text in the word document to be added to the features section of the brochure and the rest of the text has been re-worded in this document too. The logos of our product partners should also appear in the document.I'd like to use the colors and look from our website www.korventa.com.au

Target Market(s)

Government organisations, event management companies, emergency service providers, event promotion companies

Industry/Entity Type

Hire

Font styles to use
Other font styles liked:
• Helvetica

Colors
85cae6
0555a3
999999
1b1b1b
c4c4c4
0492cd

Requirements
Must have
• The product specifications and product partner logos
Nice to have
• A well laid out informative brochure that will appeal to our target market with good graphics

```html
<!DOCTYPE html>
<html lang="en">
<head>
<meta charset="utf-8">
<title>MCCC Mobile CCTV Command Centre Brochure</title>
<link href="https://fonts.googleapis.com/css2?family=Montserrat:wght@400;500;600;700&display=swap" rel="stylesheet">
<style>
  :root{
    --sky:#85cae6;
    --navy:#0555a3;
    --grey:#999999;
    --ink:#1b1b1b;
    --silver:#c4c4c4;
    --blue:#0492cd;
    --page:#ffffff;
    --stage:#c9c9c9;
  }
  *{box-sizing:border-box;margin:0;padding:0}
  html,body{width:898px;height:1200px;overflow:hidden}
  body{background:var(--stage);font-family:"Montserrat",Helvetica,Arial,sans-serif;color:var(--ink);position:relative}
  .spread{position:absolute;left:39px;width:820px;height:540px;display:flex;box-shadow:0 8px 24px rgba(0,0,0,.25);background:var(--page)}
  .spread--outer{top:30px}
  .spread--inner{top:630px}
  .panel{position:relative;width:410px;height:540px;overflow:hidden}
  .panel__bg{position:absolute;inset:0;width:100%;height:100%}
  .abs{position:absolute}
  .ph{position:absolute}

  /* back cover */
  .intro{left:130px;top:26px;width:260px;color:#fff;font-size:10.5px;font-weight:600;line-height:1.2;text-transform:uppercase;text-align:center}
  .contact-label{left:230px;top:120px;color:#fff;font-size:11px;font-weight:600;text-transform:uppercase}
  .contact{left:150px;color:#fff;font-weight:500;display:flex;align-items:center;gap:8px}
  .contact svg{flex:none}
  .contact--web{top:148px;font-size:13px}
  .contact--mail{top:174px;font-size:15px}
  .contact--phone{top:200px;font-size:22px;font-weight:600}
  .partners-title{left:36px;top:304px;font-size:13px;font-weight:500;color:var(--ink);text-transform:uppercase}
  .partner-name{left:44px;font-size:13px;font-weight:700}
  .partner-name--track{top:338px;color:var(--navy)}
  .partner-name--arvon{top:378px;color:var(--ink)}
  .partner-badge{left:58px;top:420px;width:48px;height:44px;background:var(--navy);border:2px solid #fff}
  .address{left:160px;top:400px;font-size:9.5px;color:var(--ink);display:flex;gap:8px;align-items:center;line-height:1.25}
  .site{left:160px;top:438px;font-size:15px;font-weight:600;color:var(--ink);display:flex;gap:8px;align-items:center}

  /* front cover */
  .brand{left:100px;top:28px;display:flex;align-items:center;gap:8px}
  .brand__dot{width:16px;height:16px;border-radius:50%;background:var(--blue)}
  .brand__name{font-size:12px;font-weight:700;color:var(--blue);text-transform:uppercase;letter-spacing:.3px}
  .title{left:96px;top:60px;font-size:11.5px;font-weight:600;text-transform:uppercase;color:var(--ink)}
  .rule{left:116px;top:80px;width:220px;height:1px;background:var(--blue)}
  .tagline{left:110px;top:86px;width:240px;text-align:center;font-size:10.5px;font-weight:600;color:var(--blue);line-height:1.25}
  .cover-text{left:46px;top:400px;width:330px;color:#fff;font-size:10px;line-height:1.35}

  /* inner */
  .heading{font-weight:500;text-transform:uppercase;line-height:1.05}
  .ideal-title{left:40px;top:24px;color:#fff;font-size:11px;font-weight:700}
  .list{list-style:none;font-size:8.5px;line-height:1.3}
  .list li::before{content:"\2022\00a0"}
  .list--white{color:#fff}
  .ideal-list{left:56px;top:44px;width:330px}
  .imaging-title{left:190px;top:120px;color:var(--ink);font-size:15px}
  .imaging-list{left:210px;top:166px;width:190px;color:var(--ink)}
  .imaging-list li{margin-bottom:6px}
  .mast-list{left:28px;top:300px;width:190px;color:var(--ink)}
  .mast-list li{margin-bottom:4px}
  .recording-title{left:40px;top:50px;font-size:16px;color:var(--ink)}
  .recording-list{left:70px;top:82px;width:320px;color:var(--ink)}
  .recording-list li{margin-bottom:4px}
  .power-block{left:30px;top:0}
  .power-title{left:0;top:290px;font-size:16px;color:var(--ink);white-space:nowrap}
  .power-list{left:0;top:338px;width:260px;color:var(--ink)}
  .power-list li{margin-bottom:6px}
</style>
</head>
<body>

<!-- OUTER SPREAD -->
<section class="spread spread--outer">
  <!-- back cover -->
  <div class="panel panel--back">
    <svg class="panel__bg" viewBox="0 0 410 540" aria-hidden="true">
      <defs>
        <linearGradient id="gBlue" x1="0" y1="0" x2="1" y2="1">
          <stop offset="0" stop-color="var(--blue)"/><stop offset="1" stop-color="var(--navy)"/>
        </linearGradient>
        <linearGradient id="gCity" x1="0" y1="0" x2="1" y2="1">
          <stop offset="0" stop-color="#d9dfe8"/><stop offset="0.5" stop-color="#b7c2d4"/><stop offset="1" stop-color="#e9d9d2"/>
        </linearGradient>
      </defs>
      <rect width="410" height="540" fill="url(#gCity)"/>
      <polygon points="0,60 410,0 410,360 200,470 0,240" fill="url(#gBlue)"/>
      <polygon points="210,260 410,200 410,430 240,470" fill="var(--sky)" opacity=".35"/>
    </svg>
    <div class="ph" role="img" aria-label="City traffic light trails photograph" style="left:0;top:300px;width:410px;height:240px;background:linear-gradient(160deg,rgba(205,214,230,.0),rgba(230,220,215,.55))"></div>
    <div class="ph" role="img" aria-label="Hand touching security icons photograph" style="left:0;top:80px;width:150px;height:160px;background:linear-gradient(135deg,#c7ccd6,#8d96a6);clip-path:polygon(0 0,100% 50%,0 100%)"></div>
    <p class="abs intro">Korventa Security Systems specialises in designing and installing state of the art, multi-faceted security solutions across all business sectors throughout Australia.</p>
    <p class="abs contact-label">Contact:</p>
    <p class="abs contact contact--web"><svg width="11" height="11" viewBox="0 0 12 12"><circle cx="6" cy="6" r="5" fill="none" stroke="#fff" stroke-width="1.2"/><path d="M1 6h10M6 1c-2 3-2 7 0 10M6 1c2 3 2 7 0 10" fill="none" stroke="#fff"/></svg>korventamccc.com.au</p>
    <p class="abs contact contact--mail"><svg width="12" height="9" viewBox="0 0 12 9"><rect x=".5" y=".5" width="11" height="8" fill="none" stroke="#fff"/><path d="M.5 .5 6 5l5.5-4.5" fill="none" stroke="#fff"/></svg>info@korventa.com.au</p>
    <p class="abs contact contact--phone"><svg width="16" height="16" viewBox="0 0 16 16"><path d="M3 2h3l1 4-2 1c1 2 2 3 4 4l1-2 4 1v3c0 1-1 2-2 2C7 15 1 9 1 4c0-1 1-2 2-2z" fill="#fff"/></svg>03 9000 4417</p>
    <div class="ph" role="img" aria-label="Tablet and phone showing camera feeds" style="left:230px;top:280px;width:140px;height:110px;background:linear-gradient(135deg,#1b1b1b,#33465e);border-radius:8px"></div>
    <p class="abs partners-title">Our Partners</p>
    <p class="abs partner-name partner-name--track">Tracklane</p>
    <p class="abs partner-name partner-name--arvon">Arvon Systems</p>
    <div class="abs partner-badge"></div>
    <p class="abs address"><svg width="12" height="14" viewBox="0 0 12 14"><path d="M6 1a4 4 0 0 1 4 4c0 3-4 8-4 8S2 8 2 5a4 4 0 0 1 4-4z" fill="none" stroke="var(--ink)"/><circle cx="6" cy="5" r="1.4" fill="var(--ink)"/></svg>Suite 4, Level 12, 88 Harbour Lane<br>Melbourne, Vic 3000</p>
    <p class="abs site"><svg width="13" height="13" viewBox="0 0 12 12"><circle cx="6" cy="6" r="5" fill="none" stroke="var(--ink)" stroke-width="1.2"/><path d="M1 6h10M6 1c-2 3-2 7 0 10M6 1c2 3 2 7 0 10" fill="none" stroke="var(--ink)"/></svg>korventamccc.com.au</p>
  </div>

  <!-- front cover -->
  <div class="panel panel--front">
    <svg class="panel__bg" viewBox="0 0 410 540" aria-hidden="true">
      <defs>
        <linearGradient id="gFront" x1="0" y1="0" x2="0" y2="1">
          <stop offset="0" stop-color="var(--blue)"/><stop offset="1" stop-color="var(--navy)"/>
        </linearGradient>
      </defs>
      <rect width="410" height="540" fill="#fff"/>
      <polygon points="0,0 40,0 230,330 410,290 410,540 0,540" fill="url(#gFront)"/>
      <polygon points="0,0 40,0 150,190 0,260" fill="var(--sky)" opacity=".35"/>
    </svg>
    <div class="abs brand"><span class="brand__dot"></span><span class="brand__name">Korventa Security Systems</span></div>
    <p class="abs title">MCCC- Mobile CCTV Command Centre</p>
    <div class="abs rule"></div>
    <p class="abs tagline">The Ultimate rapidly deployed<br>surveillance solution</p>
    <div class="ph" role="img" aria-label="Black command centre van with blue chequered band and camera mast" style="left:70px;top:140px;width:330px;height:220px;background:linear-gradient(160deg,#3a3f47,#111 60%,#0492cd);border-radius:18px 40px 10px 10px"></div>
    <p class="abs cover-text">The mobile CCTV Command Centre is a full electronic surveillance service for hire equipped with the latest CCTV technology to ensure that images captured are the best quality possible. Designed specifically for rapid deployment and issue response- the unit allows for the creation of a full site CCTV set-up in under 5 hours, regardless of size and location.</p>
  </div>
</section>

<!-- INNER SPREAD -->
<section class="spread spread--inner">
  <div class="panel panel--left">
    <svg class="panel__bg" viewBox="0 0 410 540" aria-hidden="true">
      <defs>
        <linearGradient id="gIn" x1="0" y1="0" x2="1" y2="1">
          <stop offset="0" stop-color="var(--blue)"/><stop offset="1" stop-color="var(--navy)"/>
        </linearGradient>
      </defs>
      <rect width="410" height="540" fill="#fff"/>
      <polygon points="30,0 410,0 410,540 250,540 200,110 60,120" fill="url(#gIn)"/>
      <polygon points="30,0 410,0 410,120 60,120" fill="var(--navy)" opacity=".6"/>
    </svg>
    <p class="abs heading ideal-title">The mobile CCTV command centre is ideal for:</p>
    <ul class="abs list list--white ideal-list">
      <li>Major and Sporting Events, Festivals, Protests and Outdoor Concerts</li>
      <li>Short term site security</li>
      <li>Crime and ASB hotspots</li>
      <li>Anywhere traditional CCTV has limited or no coverage</li>
      <li>A versatile, temporary extension to a permanently installed video surveillance system</li>
    </ul>
    <div class="ph" role="img" aria-label="Night photograph of illuminated site" style="left:40px;top:140px;width:120px;height:80px;background:linear-gradient(135deg,#1a2f6b,#e0572a 60%,#f1b13c)"></div>
    <div class="ph" role="img" aria-label="Roof mounted cameras at dusk" style="left:80px;top:205px;width:120px;height:85px;background:linear-gradient(135deg,#d59b86,#4c4e66)"></div>
    <p class="abs heading imaging-title">Imaging and<br>Communications:</p>
    <ul class="abs list imaging-list">
      <li>HD Fixed, thermal, PTZ (pan, tilt &amp; zoom) and 360 degree 4K cameras</li>
      <li>8 x Vehicle roof-mounted HD cameras for 360 degree visibility with either stationary or mobile recording capabilities</li>
      <li>8 x Rapidly deployed HD cameras with GPS, 4G and point to point transmission options</li>
    </ul>
    <ul class="abs list mast-list">
      <li>Telescopic mast to 12.5m above vehicle equipped as standard with 2 x 180 degree fixed HD cameras and 1 x long range IR PTZ camera ideal for perimeter protection</li>
      <li>7 x HD crowd controller body cameras with live streaming capabilities to enhance manpower security resources</li>
      <li>IP two-way PA systems</li>
      <li>On-board UHF2 way radio system</li>
      <li>5 Outdoor PoE networked horn speakers provide clear, long range speech for remote speaking in video surveillance applications</li>
    </ul>
    <div class="ph" role="img" aria-label="Command centre van with raised camera mast" style="left:228px;top:440px;width:182px;height:100px;background:linear-gradient(160deg,#5b6b85,#141820)"></div>
  </div>

  <div class="panel panel--right">
    <svg class="panel__bg" viewBox="0 0 410 540" aria-hidden="true">
      <defs>
        <linearGradient id="gIn2" x1="0" y1="0" x2="1" y2="1">
          <stop offset="0" stop-color="var(--blue)"/><stop offset="1" stop-color="var(--navy)"/>
        </linearGradient>
      </defs>
      <rect width="410" height="540" fill="url(#gIn2)"/>
      <polygon points="0,0 410,0 410,190 90,232 0,60" fill="#fff"/>
      <polygon points="0,260 410,200 410,430 0,520" fill="#fff"/>
    </svg>
    <p class="abs heading recording-title">Recording and Viewing:</p>
    <ul class="abs list recording-list">
      <li>A 2- person control room with observation area</li>
      <li>GPS tracking &amp; video remote viewing capability onsite or cloud based</li>
      <li>6 x 21" HD LCD monitors, 2 x 28" 4K LCD monitors &amp; on-board recording system</li>
      <li>VCA for any event (Video Content Analytics)</li>
      <li>Live streaming for effective event and incident management</li>
      <li>Veritec VMS Security Centre, Arvon communications Camera Station, Skyhawk Networks cloud VMS &amp; Tracklane incident management software</li>
    </ul>
    <div class="ph" role="img" aria-label="Abstract blue fibre optic network graphic" style="left:20px;top:200px;width:90px;height:80px;background:linear-gradient(135deg,#85cae6,#0555a3);clip-path:polygon(50% 0,100% 50%,50% 100%,0 50%)"></div>
    <div class="abs power-block">
      <p class="abs heading power-title">Power &amp;<br>Auxiliary Services:</p>
      <ul class="abs list power-list">
        <li>Complete standalone power source</li>
        <li>Generator for continuous power/ mains power capabilities</li>
        <li>Battery power to run for up to 24 hrs (solar boosted)</li>
        <li>1 Electronics technician per shift</li>
      </ul>
    </div>
    <div class="ph" role="img" aria-label="Side view of the Mobile CCTV Command Centre van under trees" style="left:0;top:410px;width:410px;height:130px;background:linear-gradient(160deg,#6c8a5a,#1b1b1b 55%,#0492cd);clip-path:polygon(0 45%,100% 0,100% 100%,0 100%)"></div>
  </div>
</section>

</body>
</html>
```